Book Cover for Notes on the Quiet River's Far Lamps

I need a book cover for a 6 x 9 paperback titled Notes on the Quiet River's Far Lamps Gathered by Sailors and Weavers Resting in the Valley beyond the Northern Valley. It has to do with consciousness, the mind, incarnation onto Earth, leaving Earth, and the life in the life after this life. I have an idea I'm providing with this description, but I am open to anything that would be striking and stimulating, whether with a book or not. I am the author, T. Warren Blakely. I've added another background idea to see if anyone can do something with it and I've increased the budget.

```html
<!DOCTYPE html>
<html lang="en">
<head>
<meta charset="UTF-8">
<title>Notes on the Quiet River's Far Lamps — T. Warren Blakely</title>
<link href="https://fonts.googleapis.com/css2?family=Cinzel:wght@400;500;600&family=Sorts+Mill+Goudy&display=swap" rel="stylesheet">
<style>
  :root {
    --sky-top: #9ca1a8;
    --sky-mid: #80858d;
    --sky-bottom: #636770;
    --title-cream: #fdf5d2;
    --ink: #0b0b0c;
    --author-white: #ffffff;
    --glow-core: #fbf1cf;
    --glow-warm: #e9cf98;
    --glow-edge: #a7845f;
  }
  html, body {
    margin: 0;
    padding: 0;
    width: 800px;
    height: 1200px;
    overflow: hidden;
    background: var(--sky-bottom);
  }
  .cover {
    position: relative;
    width: 800px;
    height: 1200px;
    overflow: hidden;
    background: linear-gradient(180deg, var(--sky-top) 0%, var(--sky-mid) 45%, var(--sky-bottom) 100%);
    text-align: center;
  }
  .title-lead {
    position: absolute;
    top: 36px;
    left: 0;
    width: 100%;
    margin: 0;
    font-family: 'Cinzel', serif;
    font-weight: 600;
    font-size: 154px;
    line-height: 1;
    letter-spacing: 6px;
    color: var(--title-cream);
    text-shadow: 0 0 14px rgba(255, 248, 220, 0.35), 2px 3px 6px rgba(40, 40, 50, 0.35);
  }
  .subtitle {
    position: absolute;
    top: 202px;
    left: 0;
    width: 100%;
    margin: 0;
    font-family: 'Sorts Mill Goudy', serif;
    font-size: 32px;
    line-height: 48px;
    color: var(--ink);
  }
  .title-close {
    position: absolute;
    top: 320px;
    left: 0;
    width: 100%;
    margin: 0;
    font-family: 'Cinzel', serif;
    font-weight: 500;
    font-size: 38px;
    line-height: 1.1;
    color: var(--ink);
  }
  .glowing-book {
    position: absolute;
    top: 560px;
    left: 10px;
    width: 780px;
    height: 350px;
  }
  .author {
    position: absolute;
    top: 1038px;
    left: 0;
    width: 100%;
    margin: 0;
    font-family: 'Cinzel', serif;
    font-weight: 500;
    font-size: 58px;
    line-height: 1;
    color: var(--author-white);
  }
</style>
</head>
<body>
  <main class="cover">
    <h1 class="title-lead">NOTES</h1>
    <p class="subtitle">on the Quiet River's Far Lamps Gathered by<br>Sailors and Weavers Resting in the</p>
    <p class="title-close">Valley beyond the Northern Valley</p>

    <svg class="glowing-book" viewBox="0 0 780 350" role="img" aria-label="An open book with glowing pages and rays of light rising from it">
      <defs>
        <radialGradient id="book-glow" cx="50%" cy="55%" r="55%">
          <stop offset="0%" stop-color="var(--glow-core)" stop-opacity="1"/>
          <stop offset="45%" stop-color="var(--glow-warm)" stop-opacity="0.85"/>
          <stop offset="80%" stop-color="var(--glow-edge)" stop-opacity="0.35"/>
          <stop offset="100%" stop-color="var(--glow-edge)" stop-opacity="0"/>
        </radialGradient>
      </defs>
      <rect x="0" y="0" width="780" height="350" fill="url(#book-glow)"/>
    </svg>

    <p class="author">T. Warren Blakely</p>
  </main>
</body>
</html>
```